Fahrzeugbeschriftung für Unternehmen in den Bereichen Gebäudetechnik, SmartHome und Regenerative Energien
Zielgruppe
Wir sind ein junges Unternehmen das sich auf Gebäudetechnik, SmartHome und Regenerative Energien spezialisiert hat.
Aufgabenstellung
Design für zwei Fahrzeuge:
- KR Lastmark L4 Kasten kurzer Radstand, Heckklappe BJ2023
- KR Bolvano Kasten Radstand mittel, Hochdach, Flügeltüren heck BJ2011
Keine Fotos im Design.
Fahrzeug Grundfarbe ist weiß
Folgende Bilder müssen verwendet werden:
- Firmenlogo
- Logo Innung
- Virelta Partnerlogo

```html
<!DOCTYPE html>
<html lang="de">
<head>
<meta charset="utf-8">
<title>Kestner Elektrotechnik – Fahrzeugbeschriftung</title>
<link rel="stylesheet" href="https://fonts.googleapis.com/css2?family=Montserrat:wght@400;600;700;800&display=swap">
<style>
  :root {
    --navy: #1f3a5f;
    --green: #4fae47;
    --white: #ffffff;
    --body-line: #c9ced4;
    --glass: #2b2f35;
    --tire: #1b1c1e;
    --rim: #e6e8ea;
    --badge-grey: #a9adb2;
    --badge-dark: #1c1c1c;
    --badge-orange: #f0a21b;
    --tail: #9c1c1c;
    --canvas: #ffffff;
  }
  html, body {
    margin: 0;
    padding: 0;
    width: 1200px;
    height: 2338px;
    overflow: hidden;
    background: var(--canvas);
  }
  .livery { display: block; width: 1200px; height: 2338px; }
  .brand { font-family: "Montserrat", sans-serif; font-weight: 800; fill: var(--navy); }
  .tagline { font-family: "Montserrat", sans-serif; font-weight: 600; fill: var(--navy); letter-spacing: 0.5em; }
  .contact { font-family: "Montserrat", sans-serif; font-weight: 700; fill: var(--white); }
  .contact-dark { font-family: "Montserrat", sans-serif; font-weight: 700; fill: var(--navy); }
  .small { font-family: "Montserrat", sans-serif; font-weight: 400; }
  .center { text-anchor: middle; }
  .van-body { fill: var(--white); stroke: var(--body-line); stroke-width: 1.5; }
  .glass { fill: var(--glass); }
  .tire { fill: var(--tire); }
  .rim { fill: var(--rim); }
  .hub { fill: var(--tire); }
  .navy { fill: var(--navy); }
  .green { fill: var(--green); }
  .badge-partner { fill: var(--badge-grey); }
  .badge-partner-end { fill: var(--badge-dark); }
  .badge-guild { fill: var(--badge-orange); }
  .bumper { fill: #1e1f21; }
  .tail-light { fill: var(--tail); }
</style>
</head>
<body>
<svg class="livery" viewBox="0 0 924 1800" xmlns="http://www.w3.org/2000/svg">
  <defs>
    <g id="side-body">
      <path class="van-body" d="M62 248 L70 222 Q120 190 228 160 L300 70 Q310 58 340 56 L790 50 Q815 50 825 75 L848 180 L860 290 L858 320 L62 325 Z"/>
      <path class="glass" d="M242 160 L300 78 L412 72 L412 168 Z"/>
      <rect class="bumper" x="58" y="252" width="90" height="72" rx="8"/>
      <rect class="bumper" x="800" y="286" width="62" height="36" rx="6"/>
      <rect class="tail-light" x="822" y="186" width="22" height="50" rx="3"/>
    </g>
    <g id="wheel">
      <circle class="tire" r="50"/>
      <circle class="rim" r="34"/>
      <circle class="hub" r="11"/>
    </g>
    <g id="badges">
      <path class="badge-partner" d="M0 0 H110 L122 26 H0 Z"/>
      <path class="badge-partner-end" d="M110 0 H145 V26 H122 Z"/>
      <rect class="badge-guild" x="2" y="36" width="58" height="24" rx="3"/>
    </g>
  </defs>

  <g class="side-left">
    <use href="#side-body"/>
    <path class="navy" d="M270 325 L842 212 L858 320 Z"/>
    <path class="green" d="M268 328 L830 190 L836 214 L330 326 Z"/>
    <rect class="navy" x="690" y="62" width="100" height="100" rx="14" transform="rotate(-13 740 112)"/>
    <text class="brand" x="262" y="262" font-size="74" transform="rotate(-13 262 262)">KESTNER</text>
    <text class="tagline" x="318" y="286" font-size="20" transform="rotate(-13 318 286)">ELEKTROTECHNIK</text>
    <text class="contact" x="444" y="292" font-size="16" transform="rotate(-13 444 292)">www.kestner-elektrotechnik.de</text>
    <text class="contact" x="480" y="313" font-size="11">+49 (0)8312 480 36 15</text>
    <use href="#badges" x="445" y="78"/>
    <use href="#wheel" x="205" y="312"/>
    <use href="#wheel" x="700" y="312"/>
  </g>

  <g class="side-right">
    <use href="#side-body" transform="translate(924 400) scale(-1 1)"/>
    <path class="navy" d="M66 610 L640 725 L66 720 Z"/>
    <path class="green" d="M90 590 L650 722 L590 724 L84 612 Z"/>
    <rect class="navy" x="118" y="462" width="110" height="110" rx="14" transform="rotate(13 173 517)"/>
    <text class="brand" x="255" y="556" font-size="74" transform="rotate(13 255 556)">KESTNER</text>
    <text class="tagline" x="282" y="610" font-size="20" transform="rotate(13 282 610)">ELEKTROTECHNIK</text>
    <text class="contact" x="162" y="618" font-size="16" transform="rotate(13 162 618)">www.kestner-elektrotechnik.de</text>
    <text class="contact" x="318" y="711" font-size="11">+49 (0)8312 480 36 15</text>
    <use href="#badges" x="332" y="477"/>
    <use href="#wheel" x="215" y="712"/>
    <use href="#wheel" x="718" y="712"/>
  </g>

  <g class="rear">
    <path class="van-body" d="M262 860 Q268 812 320 810 L604 810 Q656 812 662 860 L670 1140 L254 1140 Z"/>
    <path fill="#eef0f2" d="M286 830 Q292 820 320 820 L604 820 Q632 820 638 830 L632 945 L292 945 Z"/>
    <path class="navy" d="M252 1000 H672 V1140 H252 Z"/>
    <rect class="green" x="452" y="1000" width="220" height="20"/>
    <line x1="462" y1="810" x2="462" y2="1140" stroke="#b8bec5" stroke-width="1.2"/>
    <text class="small" x="372" y="840" font-size="10" fill="#8d99a8" letter-spacing="1">INNOVATIVE <tspan fill="var(--green)">LÖSUNGEN</tspan></text>
    <rect class="navy" x="556" y="852" width="46" height="46" rx="8"/>
    <text class="brand" x="306" y="886" font-size="40">KESTNER</text>
    <text class="tagline" x="308" y="904" font-size="12">ELEKTROTECHNIK</text>
    <text class="contact-dark" x="333" y="930" font-size="13">www.kestner-elektrotechnik.de</text>
    <use href="#badges" x="296" y="958"/>
    <text class="contact" x="464" y="1015" font-size="13">+49 (0)8312 480 36 15</text>
    <circle cx="475" cy="1043" r="4" fill="none" stroke="var(--green)" stroke-width="1.5"/>
    <text class="small" x="484" y="1047" font-size="8" fill="#ffffff">Am Lindenfeld 4, 88170 Weiler</text>
    <rect fill="#d9dde1" x="308" y="1024" width="124" height="24" rx="2"/>
    <text class="contact" x="260" y="1092" font-size="12">GEBÄUDETECHNIK <tspan fill="var(--green)">•</tspan> SMARTHOME <tspan fill="var(--green)">•</tspan> REGENERATIVE ENERGIEN</text>
    <rect class="tail-light" x="244" y="988" width="40" height="72" rx="6"/>
    <rect class="tail-light" x="632" y="988" width="40" height="72" rx="6"/>
    <rect class="bumper" x="244" y="1124" width="428" height="44" rx="8"/>
    <rect class="tire" x="252" y="1168" width="66" height="66" rx="10"/>
    <rect class="tire" x="598" y="1168" width="66" height="66" rx="10"/>
  </g>

  <g class="front">
    <path class="van-body" d="M270 1420 Q290 1310 340 1302 L584 1302 Q634 1310 654 1420 L656 1700 L268 1700 Z"/>
    <path class="glass" d="M300 1418 L332 1322 L592 1322 L624 1418 Z"/>
    <rect class="bumper" x="242" y="1400" width="42" height="30" rx="8"/>
    <rect class="bumper" x="640" y="1400" width="42" height="30" rx="8"/>
    <rect class="navy" x="442" y="1440" width="36" height="36" rx="7"/>
    <text class="brand center" x="462" y="1504" font-size="28">KESTNER</text>
    <text class="tagline center" x="464" y="1516" font-size="8">ELEKTROTECHNIK</text>
    <text class="contact-dark small center" x="462" y="1528" font-size="7">www.kestner-elektrotechnik.de</text>
    <rect fill="#d3d7db" x="266" y="1512" width="70" height="40" rx="6"/>
    <rect fill="#d3d7db" x="588" y="1512" width="70" height="40" rx="6"/>
    <rect class="bumper" x="336" y="1536" width="252" height="42" rx="4"/>
    <rect class="bumper" x="262" y="1578" width="400" height="110" rx="12"/>
    <rect fill="#d9dde1" x="398" y="1650" width="128" height="26" rx="2"/>
  </g>
</svg>
</body>
</html>
```